FREE BBQ for life if you win our business with your creative menu design

Looking for a 11x17 size menu. we are a full service BBQ restaurant. We have an upscale environment as well as up scale service. We offer 5 star dinning at a casual price. we are on route 66 and are proud of that. we offer the finest smoked meats. Specializing in smoked pork beef and bison. we have an old barn wood decor. we only use oak to smoke our meats. use a lot of tarnished metal as well as some string nail art. Looking for a menu that goes along our style. i have attached as many pictures as i could to give you a fill of how we do it out here.
PLEASE USE THE 11"X17" MENU TEMPLATE ATTACHED IN THE PROJECT BRIEF.
Target Market(s)
Cool people and there families.
Industry/Entity Type
Business
Requirements
Must have
- I have attached the Current menu we use. File pollards menu pub. Those are all the Items. There will be some changes as we but together the new menu. The prices are changing. but that should be an easy change as we go.
Nice to have
- We are getting away from the lunch dinner menu and going to an all day menu. so rather than coming with toast or bun we will now be asking as an option. I have attached a menu i tried to make as a sample of how we will be doing it. new menu single page and new menu single page flame. These are ideas i had but could not really make it work. so use them as an idea of what we are looking for but be creative.

```html
<!DOCTYPE html>
<html lang="en">
<head>
<meta charset="utf-8">
<title>Pollards Barbeque Menu</title>
<link href="https://fonts.googleapis.com/css2?family=Rye&family=Righteous&family=Courier+Prime:wght@400;700&display=swap" rel="stylesheet">
<style>
  :root {
    --parchment: #e9c98f;
    --parchment-dark: #c99a55;
    --panel: #f3dcae;
    --red: #b3201b;
    --red-dark: #8c1410;
    --navy: #1f3f74;
    --navy-dark: #132a52;
    --gold: #e8b04a;
    --ink: #3a2412;
    --white: #fbf6ea;
  }
  * { box-sizing: border-box; margin: 0; padding: 0; }
  html, body { width: 778px; height: 1200px; overflow: hidden; background: var(--parchment); }
  .menu {
    position: relative; width: 778px; height: 1200px; overflow: hidden;
    background: radial-gradient(ellipse at 50% 50%, #f0d5a0 0%, var(--parchment) 55%, var(--parchment-dark) 100%);
    font-family: "Courier Prime", monospace; color: var(--ink);
  }
  .masthead { position: absolute; left: 0; top: 0; width: 778px; height: 170px; }
  .brand-mark {
    position: absolute; left: 0; top: 0; width: 150px; height: 140px;
    background: var(--navy-dark);
    display: flex; align-items: center; justify-content: center; gap: 8px;
  }
  .brand-mark .dot { width: 14px; height: 14px; border-radius: 50%; background: var(--red); }
  .brand-mark span { font-family: "Rye", serif; color: var(--white); font-size: 22px; }
  .name-line {
    position: absolute; left: 315px; top: 14px;
    font-family: "Rye", serif; font-size: 34px; color: var(--red); letter-spacing: 2px;
  }
  .title-band {
    position: absolute; left: 190px; top: 55px; width: 560px; height: 70px;
    background: var(--navy); border: 4px solid var(--red); border-radius: 4px;
    display: flex; align-items: center; justify-content: center;
    font-family: "Rye", serif; font-size: 54px; color: var(--white); letter-spacing: 4px;
  }
  .tagline {
    position: absolute; left: 235px; top: 128px; width: 470px; height: 30px;
    background: var(--red-dark); border: 2px solid var(--navy);
    display: flex; align-items: center; justify-content: center;
    font-family: "Rye", serif; font-size: 17px; color: var(--gold); letter-spacing: 2px;
  }
  .panel {
    position: absolute; background: var(--panel);
    border: 2px solid var(--red); border-radius: 12px;
    box-shadow: inset 0 0 0 5px var(--panel), inset 0 0 0 6px var(--red);
    padding: 18px 22px;
  }
  .panel h2 {
    font-family: "Righteous", sans-serif; font-weight: 400; color: var(--red);
    font-size: 30px; text-align: center; margin-bottom: 12px; letter-spacing: 1px;
  }
  .appetizers { left: 20px; top: 180px; width: 312px; height: 560px; }
  .bison { left: 345px; top: 180px; width: 420px; height: 395px; }
  .smoked { left: 345px; top: 585px; width: 420px; height: 585px; }
  .item { margin-bottom: 10px; }
  .item h3 { font-family: "Courier Prime", monospace; font-weight: 700; color: var(--red); font-size: 13px; }
  .item p { font-size: 10.5px; line-height: 1.3; }
  .intro { display: flex; gap: 10px; align-items: center; margin-bottom: 12px; }
  .intro .seal { flex: 0 0 44px; height: 44px; border-radius: 50%; background: var(--red-dark); }
  .intro p { font-size: 10.5px; line-height: 1.3; }
  .smoked h2 { margin-bottom: 6px; }
  .smoked .item { margin-bottom: 7px; }
</style>
</head>
<body>
<main class="menu">
  <header class="masthead">
    <div class="brand-mark"><i class="dot"></i><span>Pollards</span></div>
    <div class="name-line">POLLARDS</div>
    <div class="title-band">BARBEQUE</div>
    <div class="tagline">SMOKED PORK, BEEF &amp; BISON</div>
  </header>

  <section class="panel appetizers">
    <h2>appetizers</h2>
    <div class="item"><h3>King Rings</h3><p>Green Chili battered fried golden crispy 1" thick onion rings. 6.99</p></div>
    <div class="item"><h3>Deep Fried Pickles</h3><p>Crisp dill pickle chips battered and fried to a golden crisp, served with ranch. 6.99</p></div>
    <div class="item"><h3>Fried Okra</h3><p>Okra is breaded then fried until golden. 6.99</p></div>
    <div class="item"><h3>Green Chili Waffle Fries</h3><p>Crispy waffle-cut fries, topped with a savory blend of cheese and New Mexico green chile. 7.99</p></div>
    <div class="item"><h3>PB Wild Wings</h3><p>Big meaty pork wings, deep fried to a perfect golden brown, tossed in a hot and tangy buffalo-style sauce and served with spicy buttermilk ranch dressing on the side. 9.99</p></div>
    <div class="item"><h3>Sampler Platter</h3><p>Two PB Wild Wings, one Fried Pickles, 2 King Rings. 7.99</p></div>
  </section>

  <section class="panel bison">
    <h2>bison</h2>
    <div class="intro"><i class="seal"></i><p>Comes with 1 side and your choice of Texas toast, Kaiser bun, Whole wheat bread or Gluten free bread.</p></div>
    <div class="item"><h3>Bison Brisket</h3><p>The belly of beast, smoked then sliced thin and grilled. Juicy and tender. 18.99</p></div>
    <div class="item"><h3>Bison Burger</h3><p>Smoked, then grilled served with pepper jack cheese, lettuce, tomato, pickle, topped with spicy sauce. 12.99</p></div>
    <div class="item"><h3>Bison Steak</h3><p>7oz of lean healthy meat cooked to your desired temp. 24.99</p></div>
  </section>

  <section class="panel smoked">
    <h2>smoked</h2>
    <div class="intro"><i class="seal"></i><p>Comes with 1 side and your choice of Texas toast, Kaiser bun, Whole wheat bread or Gluten free bread.</p></div>
    <div class="item"><h3>Baby Back Ribs</h3><p>Tender to the bone, finger licking good, never need a knife, best ribs you'll ever have. Full Rack 19.99 Half Rack 12.99</p></div>
    <div class="item"><h3>St. Louis Ribs</h3><p>A nice big tender spare rib, slow smoked to tender that you can pull your teeth into. 16.99</p></div>
    <div class="item"><h3>Beef Brisket</h3><p>The most tender mouth watering smoky moist, succulent piece of meat you can find. 15.99</p></div>
    <div class="item"><h3>Pulled Pork</h3><p>Smoked for 14-18 hrs then pulled and mixed with our signature home barbeque sauce. 13.99</p></div>
    <div class="item"><h3>Sliced Pork</h3><p>Smoked juicy tenderloin sliced thin then grilled per order. 13.99</p></div>
    <div class="item"><h3>Smoked Turkey</h3><p>Breast meat smoked and sliced juicy and tender. 13.99</p></div>
    <div class="item"><h3>Smoked Chicken half</h3><p>Moist and juicy smoked thigh and breast with our signature sauce on the grill. 12.99</p></div>
    <div class="item"><h3>Rib Tips</h3><p>Slow oak smoked tips tossed in our house sauce. 11.99</p></div>
  </section>
</main>
</body>
</html>
```